Marta Belcourt Name Card Design

Hello Designers,
I wanna have a name card with these details below:
Name: Marta Belcourt
Job Title: Doctor
Address: 2318 Ferris Lane, Tacoma, WA, US
Phone: 8273360915
Slogan on card: Health care 24/7, Whenever you need, we're there!
I love yellows colors, red and white. It would be nice if my card would be designed with these colors.

```html
<!DOCTYPE html>
<html lang="en">
<head>
<meta charset="utf-8">
<title>Marta Belcourt – Name Card</title>
<link href="https://fonts.googleapis.com/css2?family=Source+Sans+3:ital,wght@0,400;0,600;0,700;1,400&display=swap" rel="stylesheet">
<style>
  :root {
    --backdrop: #111111;
    --sun-yellow: #fff200;
    --signal-red: #ed1c24;
    --ink: #000000;
    --paper: #ffffff;
    --slate: #58595b;
    --rule: #8a8a8a;
  }
  * { margin: 0; padding: 0; box-sizing: border-box; }
  html, body { width: 1183px; height: 1200px; overflow: hidden; }
  body {
    position: relative;
    background: var(--backdrop);
    font-family: "Source Sans 3", "Myriad Pro", Arial, sans-serif;
  }
  .abs { position: absolute; white-space: nowrap; line-height: 1; }

  /* Front card */
  .card-front { position: absolute; left: 68px; top: 113px; width: 789px; height: 449px; overflow: hidden; background: var(--sun-yellow); }
  .red-band { position: absolute; left: 0; top: 284px; width: 789px; height: 165px; background: var(--signal-red); }
  .pulse-graphic {
    position: absolute; left: 609px; top: 170px; width: 129px; height: 234px;
    background: linear-gradient(180deg, var(--signal-red) 0%, #f68a12 50%, var(--sun-yellow) 100%);
  }
  .holder-name { left: 36px; top: 48px; font-size: 62px; font-weight: 700; color: var(--ink); letter-spacing: -0.5px; }
  .holder-role { left: 36px; top: 110px; font-size: 54px; font-weight: 400; color: var(--ink); }
  .tagline { left: 40px; top: 205px; font-size: 26.5px; color: var(--ink); display: flex; align-items: center; gap: 4px; }
  .hours-badge {
    display: inline-block; width: 40px; height: 40px; border-radius: 50%;
    border: 2px solid var(--signal-red);
  }
  .contact { left: 40px; font-size: 23px; color: var(--paper); }
  .contact-address { top: 340px; }
  .contact-phone { top: 382px; display: flex; align-items: center; gap: 6px; }

  /* Back card */
  .card-back { position: absolute; left: 238px; top: 588px; width: 876px; height: 499px; background: var(--paper); color: var(--slate); }
  .back-title { left: 56px; top: 67px; font-size: 28px; font-weight: 700; letter-spacing: 0.3px; }
  .field-label { font-size: 27px; }
  .dotted-rule { position: absolute; border-bottom: 1.5px dotted var(--rule); height: 0; }
  .entry-box { position: absolute; border: 1.5px solid var(--slate); border-radius: 3px; }
  .day-label { font-size: 28px; font-weight: 600; }
  .back-slogan { left: 56px; top: 429px; font-size: 27.5px; font-style: italic; }
</style>
</head>
<body>

<section class="card-front" aria-label="Name card front">
  <div class="red-band"></div>
  <div class="pulse-graphic" role="img" aria-label="Heartbeat pulse line graphic"></div>
  <div class="abs holder-name">Marta Belcourt</div>
  <div class="abs holder-role">Doctor</div>
  <div class="abs tagline">
    <span>Health care</span>
    <span class="hours-badge" role="img" aria-label="24/7 clock badge"></span>
    <span>Whenever you need, we're there!</span>
  </div>
  <div class="abs contact contact-address">2318 Ferris Lane, Tacoma, WA, US</div>
  <div class="abs contact contact-phone">
    <svg width="20" height="20" viewBox="0 0 20 20" aria-label="Phone">
      <circle cx="10" cy="10" r="8.5" fill="none" stroke="var(--paper)" stroke-width="1.3"/>
      <path d="M7,5 C5,7 6,12 9,14.5 C11,16 13,15 13.5,14 L12,12 L10.5,12.5 C9.5,11.5 8.5,10 8.3,8.5 L9.5,7.5 L8.5,5 Z" fill="var(--paper)"/>
    </svg>
    <span>8273360915</span>
  </div>
</section>

<section class="card-back" aria-label="Appointment card back">
  <div class="abs back-title">YOUR APPOINTMENT</div>

  <div class="abs field-label" style="left:60px;top:153px;">Name :</div>
  <div class="dotted-rule" style="left:157px;top:174px;width:485px;"></div>

  <div class="abs field-label" style="left:60px;top:216px;">Date :</div>
  <div class="dotted-rule" style="left:157px;top:236px;width:158px;"></div>
  <div class="abs field-label" style="left:326px;top:216px;">Time :</div>
  <div class="dotted-rule" style="left:400px;top:236px;width:148px;"></div>
  <div class="abs field-label" style="left:554px;top:216px;">am / pm</div>

  <div class="abs field-label" style="left:60px;top:278px;">Next Appointment</div>
  <div class="entry-box" style="left:294px;top:275px;width:156px;height:33px;"></div>
  <div class="entry-box" style="left:504px;top:275px;width:157px;height:33px;"></div>

  <div class="abs day-label" style="left:55px;top:361px;">MON</div>
  <div class="entry-box" style="left:128px;top:361px;width:53px;height:31px;"></div>
  <div class="abs day-label" style="left:195px;top:361px;">TUE</div>
  <div class="entry-box" style="left:254px;top:361px;width:54px;height:31px;"></div>
  <div class="abs day-label" style="left:322px;top:361px;">WED</div>
  <div class="entry-box" style="left:391px;top:361px;width:54px;height:31px;"></div>
  <div class="abs day-label" style="left:459px;top:361px;">THU</div>
  <div class="entry-box" style="left:522px;top:361px;width:54px;height:31px;"></div>
  <div class="abs day-label" style="left:590px;top:361px;">FRI</div>
  <div class="entry-box" style="left:639px;top:361px;width:54px;height:31px;"></div>
  <div class="abs day-label" style="left:706px;top:361px;">SAT</div>
  <div class="entry-box" style="left:763px;top:361px;width:54px;height:31px;"></div>

  <div class="abs back-slogan">Health care 24/7, Whenever you need, we’re there!</div>
</section>

</body>
</html>
```